Design for sports training app

We need the design for 9 screens of an app that supports trainers of sport teams in preparing their training sessions. Regarding colors, fonts etc. there is absolute freedom for the designer to choose what he thinks is best.
The app will be called "Vellix", our idea for the logo is something like a stopwatch.
Wireframes are attached for every screen. You don't have to stick to those - if you have better ideas, we are happy to see them.
Our strategy is "mobile first". Based on the app design we will create a homepage later - I guess it makes sense to give this to the same person, let's see.
The deliverables are attached.
All in all the main target is to present a very simple, intuitive and nice UI that the user can work with without much learning.
Updates
Target Market(s)
Soccer trainers
Industry/Entity Type
Training
Look and feel

```html
<!DOCTYPE html>
<html lang="en">
<head>
<meta charset="utf-8">
<title>Offensive 2 vs 1 – Training Screens</title>
<link href="https://fonts.googleapis.com/css2?family=Roboto:wght@400;500&family=Roboto+Condensed:wght@300;400&display=swap" rel="stylesheet">
<style>
  :root {
    --page-bg: #f1f1f2;
    --bar-bg: #f7f7f8;
    --tab-bg: #e6e6ea;
    --ink: #111111;
    --brand-blue: #1f5fa8;
    --deep-top: #2b6bb6;
    --deep-bottom: #0b2a6c;
    --meter-fill: #5fa8dc;
    --white: #ffffff;
    --icon-idle: #b3b3b8;
    --battery: #35d24a;
    --pitch: #3f8f2a;
    --pitch-dark: #2f7420;
  }
  * { box-sizing: border-box; margin: 0; padding: 0; }
  html, body { width: 1200px; height: 800px; overflow: hidden; background: var(--page-bg); }
  body { font-family: "Roboto Condensed", "Arial Narrow", sans-serif; }

  .screens { position: relative; width: 1200px; height: 800px; }
  .screen {
    position: absolute; top: 116px; width: 320px; height: 568px;
    display: flex; flex-direction: column; overflow: hidden;
    box-shadow: 0 10px 30px rgba(0,0,0,0.12);
  }
  .screen--info { left: 40px; }
  .screen--stats { left: 440px; }
  .screen--gear { left: 840px; }

  .status-bar {
    height: 20px; background: var(--bar-bg); color: var(--ink);
    font-family: "Roboto", sans-serif; font-size: 11px; font-weight: 500;
    display: flex; align-items: center; justify-content: space-between; padding: 0 6px;
  }
  .status-bar .signal { letter-spacing: -1px; font-size: 9px; }
  .status-bar .signal b { letter-spacing: 0; font-size: 11px; margin-left: 4px; font-weight: 500; }
  .status-bar .power { display: flex; align-items: center; gap: 4px; }
  .battery { width: 24px; height: 10px; border: 1px solid #555; border-radius: 2px; padding: 1px; position: relative; }
  .battery::before { content: ""; display: block; width: 100%; height: 100%; background: var(--battery); border-radius: 1px; }
  .battery::after { content: ""; position: absolute; right: -3px; top: 2px; width: 2px; height: 4px; background: #555; }

  .nav-bar {
    height: 44px; background: var(--bar-bg); position: relative;
    display: flex; align-items: center; justify-content: center;
    border-bottom: 1px solid #dcdce0;
  }
  .nav-bar .back { position: absolute; left: 16px; top: 14px; }
  .nav-bar .title { color: var(--brand-blue); font-size: 14px; font-weight: 400; }

  .content {
    flex: 1; background: linear-gradient(180deg, var(--deep-top) 0%, var(--deep-bottom) 100%);
    position: relative; color: var(--white);
  }

  .tab-bar {
    height: 49px; background: var(--tab-bg);
    display: flex; justify-content: space-around; align-items: center; padding: 0 20px;
  }
  .tab-bar svg { width: 34px; height: 30px; }

  /* Info screen */
  .drill-diagram {
    position: absolute; left: 35px; top: 35px; width: 250px; height: 112px;
    border: 2px solid var(--white);
    background: linear-gradient(180deg, var(--pitch) 0%, var(--pitch-dark) 100%);
  }
  .drill-tags {
    position: absolute; left: 35px; top: 167px; width: 250px; height: 40px;
    display: flex; align-items: center; justify-content: center; gap: 16px;
  }
  .drill-tags::before, .drill-tags::after {
    content: ""; position: absolute; top: 19px; width: 44px; height: 2px; background: var(--white);
  }
  .drill-tags::before { left: 0; }
  .drill-tags::after { right: 0; }
  .tag {
    width: 40px; height: 40px; background: var(--white); border-radius: 8px;
    color: var(--brand-blue); display: flex; flex-direction: column; align-items: center; justify-content: center;
    line-height: 1;
  }
  .tag .tag-name { font-size: 9.5px; }
  .tag .tag-sub { font-size: 4.5px; margin-top: 2px; }
  .drill-text {
    position: absolute; left: 38px; top: 228px; width: 250px;
    font-size: 7.4px; line-height: 1.32; letter-spacing: -0.1px;
  }
  .drill-video {
    position: absolute; left: 35px; top: 283px; width: 250px; height: 112px;
    border: 2px solid var(--white);
    background: linear-gradient(180deg, #5d7c4a 0%, #6d9a56 45%, #5a9b4a 100%);
    display: flex; align-items: center; justify-content: center;
  }
  .play { width: 26px; height: 26px; border-radius: 50%; background: rgba(0,0,0,0.75);
    display: flex; align-items: center; justify-content: center; }

  /* Stats screen */
  .skill-list { position: absolute; left: 37px; top: 20px; width: 246px; }
  .skill { margin-bottom: 8px; }
  .skill-label { text-align: center; font-size: 9.5px; height: 16px; line-height: 16px; }
  .meter { height: 29px; border-radius: 15px; background: var(--white); overflow: hidden; }
  .meter-fill { height: 100%; background: var(--meter-fill); }

  /* Equipment screen */
  .gear-list { position: absolute; left: 37px; top: 37px; width: 246px; list-style: none; }
  .gear-item {
    height: 28px; border-radius: 14px; background: var(--white); margin-bottom: 5px;
    color: var(--brand-blue); font-size: 10.5px;
    display: flex; align-items: center; justify-content: space-between; padding: 0 22px 0 18px;
  }
</style>
</head>
<body>
<main class="screens">

  <!-- Drill info -->
  <section class="screen screen--info">
    <div class="status-bar"><span class="signal">●●●●●<b>3G</b></span><span>1:52</span><span class="power">100 % <span class="battery"></span></span></div>
    <header class="nav-bar">
      <svg class="back" width="10" height="16" viewBox="0 0 10 16"><path d="M8 1 L2 8 L8 15" fill="none" stroke="#1f5fa8" stroke-width="1.6"/></svg>
      <h1 class="title">Offensive 2 vs 1</h1>
    </header>
    <div class="content">
      <div class="drill-diagram" role="img" aria-label="Drill diagram on a green pitch showing player positions and running arrows"></div>
      <div class="drill-tags">
        <div class="tag"><span class="tag-name">LOREM</span><span class="tag-sub">34</span></div>
        <div class="tag"><span class="tag-name">IPSUM</span><span class="tag-sub">LOREM</span></div>
        <div class="tag"><span class="tag-name">DOLOR</span><span class="tag-sub">LOREM IPS</span></div>
      </div>
      <p class="drill-text">Lorem ipsum dolor sit amet, consectetur adipiscing elit. Aliquam sed dignissim elit. Maecenas in est massa. Proin condimentum, odio ut vestibulum sagittis, nunc neque ullamcorper massa, a lacinia turpis tortor sed lacus. Maecenas quis turpis venenatis, consectetur magna et, auctor odio. In dapibus leo velit.</p>
      <div class="drill-video" role="img" aria-label="Video thumbnail of players competing for the ball on a training pitch">
        <span class="play"><svg width="12" height="12" viewBox="0 0 12 12"><path d="M3 1 L11 6 L3 11 Z" fill="#fff"/></svg></span>
      </div>
    </div>
    <nav class="tab-bar">
      <svg viewBox="0 0 34 30"><circle cx="17" cy="15" r="13" fill="none" stroke="#1f5fa8" stroke-width="1.4"/><line x1="17" y1="12" x2="17" y2="23" stroke="#1f5fa8" stroke-width="1.4"/><circle cx="17" cy="8.5" r="1.1" fill="#1f5fa8"/></svg>
      <svg viewBox="0 0 34 30"><path d="M3 22 L10 15 L16 20 L29 9" fill="none" stroke="#b3b3b8" stroke-width="1.4"/><circle cx="10" cy="15" r="2" fill="var(--tab-bg)" stroke="#b3b3b8" stroke-width="1.2"/><circle cx="16" cy="20" r="2" fill="var(--tab-bg)" stroke="#b3b3b8" stroke-width="1.2"/><path d="M24 8 L30 8 L30 14" fill="none" stroke="#b3b3b8" stroke-width="1.4"/></svg>
      <svg viewBox="0 0 34 30"><path d="M17 5 L30 11 L17 17 L4 11 Z" fill="none" stroke="#b3b3b8" stroke-width="1.3"/><path d="M4 15 L17 21 L30 15" fill="none" stroke="#b3b3b8" stroke-width="1.3"/><path d="M4 19 L17 25 L30 19" fill="none" stroke="#b3b3b8" stroke-width="1.3"/></svg>
    </nav>
  </section>

  <!-- Skill stats -->
  <section class="screen screen--stats">
    <div class="status-bar"><span class="signal">●●●●●<b>3G</b></span><span>1:52</span><span class="power">100 % <span class="battery"></span></span></div>
    <header class="nav-bar">
      <svg class="back" width="10" height="16" viewBox="0 0 10 16"><path d="M8 1 L2 8 L8 15" fill="none" stroke="#1f5fa8" stroke-width="1.6"/></svg>
      <h1 class="title">Offensive 2 vs 1</h1>
    </header>
    <div class="content">
      <div class="skill-list">
        <div class="skill"><div class="skill-label">Coordination</div><div class="meter"><div class="meter-fill" style="width:75%"></div></div></div>
        <div class="skill"><div class="skill-label">Finishing</div><div class="meter"><div class="meter-fill" style="width:50%"></div></div></div>
        <div class="skill"><div class="skill-label">Stamina</div><div class="meter"><div class="meter-fill" style="width:72%"></div></div></div>
        <div class="skill"><div class="skill-label">Speed</div><div class="meter"><div class="meter-fill" style="width:89%"></div></div></div>
        <div class="skill"><div class="skill-label">Understanding of the game</div><div class="meter"><div class="meter-fill" style="width:40%"></div></div></div>
        <div class="skill"><div class="skill-label">Defensing Behavior</div><div class="meter"><div class="meter-fill" style="width:50%"></div></div></div>
      </div>
    </div>
    <nav class="tab-bar">
      <svg viewBox="0 0 34 30"><circle cx="17" cy="15" r="13" fill="none" stroke="#b3b3b8" stroke-width="1.4"/><line x1="17" y1="12" x2="17" y2="23" stroke="#b3b3b8" stroke-width="1.4"/><circle cx="17" cy="8.5" r="1.1" fill="#b3b3b8"/></svg>
      <svg viewBox="0 0 34 30"><path d="M3 22 L10 15 L16 20 L29 9" fill="none" stroke="#1f5fa8" stroke-width="1.4"/><circle cx="10" cy="15" r="2" fill="var(--tab-bg)" stroke="#1f5fa8" stroke-width="1.2"/><circle cx="16" cy="20" r="2" fill="var(--tab-bg)" stroke="#1f5fa8" stroke-width="1.2"/><path d="M24 8 L30 8 L30 14" fill="none" stroke="#1f5fa8" stroke-width="1.4"/></svg>
      <svg viewBox="0 0 34 30"><path d="M17 5 L30 11 L17 17 L4 11 Z" fill="none" stroke="#b3b3b8" stroke-width="1.3"/><path d="M4 15 L17 21 L30 15" fill="none" stroke="#b3b3b8" stroke-width="1.3"/><path d="M4 19 L17 25 L30 19" fill="none" stroke="#b3b3b8" stroke-width="1.3"/></svg>
    </nav>
  </section>

  <!-- Equipment -->
  <section class="screen screen--gear">
    <div class="status-bar"><span class="signal">●●●●●<b>3G</b></span><span>1:52</span><span class="power">100 % <span class="battery"></span></span></div>
    <header class="nav-bar">
      <svg class="back" width="10" height="16" viewBox="0 0 10 16"><path d="M8 1 L2 8 L8 15" fill="none" stroke="#1f5fa8" stroke-width="1.6"/></svg>
      <h1 class="title">Offensive 2 vs 1</h1>
    </header>
    <div class="content">
      <ul class="gear-list">
        <li class="gear-item"><span>Cones</span><span>20</span></li>
        <li class="gear-item"><span>Goals</span><span>5</span></li>
        <li class="gear-item"><span>Players</span><span>10</span></li>
        <li class="gear-item"><span>Goalies</span><span>2</span></li>
      </ul>
    </div>
    <nav class="tab-bar">
      <svg viewBox="0 0 34 30"><circle cx="17" cy="15" r="13" fill="none" stroke="#b3b3b8" stroke-width="1.4"/><line x1="17" y1="12" x2="17" y2="23" stroke="#b3b3b8" stroke-width="1.4"/><circle cx="17" cy="8.5" r="1.1" fill="#b3b3b8"/></svg>
      <svg viewBox="0 0 34 30"><path d="M3 22 L10 15 L16 20 L29 9" fill="none" stroke="#b3b3b8" stroke-width="1.4"/><circle cx="10" cy="15" r="2" fill="var(--tab-bg)" stroke="#b3b3b8" stroke-width="1.2"/><circle cx="16" cy="20" r="2" fill="var(--tab-bg)" stroke="#b3b3b8" stroke-width="1.2"/><path d="M24 8 L30 8 L30 14" fill="none" stroke="#b3b3b8" stroke-width="1.4"/></svg>
      <svg viewBox="0 0 34 30"><path d="M17 5 L30 11 L17 17 L4 11 Z" fill="none" stroke="#1f5fa8" stroke-width="1.3"/><path d="M4 15 L17 21 L30 15" fill="none" stroke="#1f5fa8" stroke-width="1.3"/><path d="M4 19 L17 25 L30 19" fill="none" stroke="#1f5fa8" stroke-width="1.3"/></svg>
    </nav>
  </section>

</main>
</body>
</html>
```